Zielgruppe
Wir sind ein klassisches IT Systemhaus und betreuen in unserer Region kleine und mittelständische Unternehmen sowie öffentliche Einrichtungen.
Aufgabenstellung
Es soll ein modernes Desigm, eine moderne Menüführung vorhanden sein. Dabei soll ein Megamenü eingebunden werden

```html
<!DOCTYPE html>
<html lang="de">
<head>
<meta charset="utf-8">
<title>Systemhaus Brandhoff – Webdesign</title>
<link href="https://fonts.googleapis.com/css2?family=Poppins:wght@300;400;500;600&display=swap" rel="stylesheet">
<style>
:root{
  --stage:#4b4b4b;
  --blue:#5687c7;
  --blue-dark:#3f6fb0;
  --link:#4f82c4;
  --text:#2b2b2b;
  --muted:#8a8a8a;
  --card:#e0dfe4;
  --rose:#f1e2e0;
  --band:#e6edf7;
  --line:#d4d4d4;
  --white:#ffffff;
}
*{box-sizing:border-box;margin:0;padding:0}
html,body{width:747px;height:1200px;overflow:hidden;background:var(--stage)}
body{font-family:'Poppins',sans-serif;color:var(--text);font-weight:300}
.stage{position:absolute;left:0;top:0;width:1512px;height:2428px;transform:scale(.494);transform-origin:0 0;background:var(--stage)}
.page{position:absolute;width:625px;background:var(--white);overflow:hidden}
.a{position:absolute}
.topbar{left:0;top:0;width:625px;height:24px;background:var(--blue);color:var(--white);font-size:10px;font-weight:400}
.topbar span{position:absolute;top:6px}
.header{left:0;top:24px;width:625px;height:57px}
.brand{left:45px;top:14px;font-size:16px;font-weight:500;color:#3a4f7a;letter-spacing:1.5px}
.brand small{display:block;font-size:5.5px;letter-spacing:3px;font-weight:400;margin-top:-2px}
.brand-dot{left:170px;top:9px;width:36px;height:36px;border-radius:50%;background:#8a949e;border:3px solid #c7ccd2}
.nav{top:20px;font-size:10.5px;font-weight:400;color:#333}
.hero{left:0;top:81px;width:625px;height:284px;background:radial-gradient(ellipse at 35% 110%,#4f73b0 0%,#20376e 45%,#0f1d45 100%)}
.hero-shade{left:324px;top:0;width:301px;height:284px;background:rgba(70,105,170,.35)}
.hero h1{left:348px;top:68px;font-size:16px;font-weight:400;color:var(--white)}
.hero p{left:348px;top:98px;width:230px;font-size:9.5px;line-height:15px;color:#e4ecf8}
.btn-blue{background:var(--blue);color:var(--white);font-size:9.5px;font-weight:400;text-align:center}
.arrow{width:25px;height:25px;border:1px solid var(--white);border-radius:50%}
.center{text-align:center}
.h-mid{font-size:11.5px;font-weight:400;line-height:17px}
.card{width:175px;height:130px;background:var(--card);font-size:9.5px;line-height:15px;text-align:center;padding:24px 12px 0}
.card b{font-weight:600}
.btn-out{border:1px solid #777;background:var(--white);font-size:9.5px;text-align:center;width:54px;height:20px;line-height:18px;left:60px;top:84px}
.hr{height:1px;background:var(--line)}
.media{background:linear-gradient(135deg,#9fb0c2,#6d7f93)}
.body-s{font-size:9.5px;line-height:15px}
.news-t{font-size:11.5px;font-weight:400;line-height:17px}
.date{font-size:7.5px;color:#aaa}
.input{width:219px;height:14px;border:1px solid #c9c9c9;font-size:7.5px;color:#aaa;padding-left:4px;line-height:12px}
.city{font-size:10px;color:var(--link);font-weight:400}
.footer{left:0;width:625px;height:211px;background:var(--blue);color:var(--white)}
.footer .brand{color:var(--white);left:48px;top:20px;font-size:15px}
.f-big{font-size:11.5px;font-weight:400;line-height:17px}
.f-s{font-size:7.5px;line-height:12.5px}
.f-link{font-size:8px;line-height:19.5px}
.f-r{font-size:10px;font-weight:400;line-height:24px}
.sq{display:inline-block;width:15px;height:15px;background:var(--white);border-radius:2px;margin-right:4px}
.crumb{font-size:10px;font-weight:400}
.select{width:170px;height:20px;border:1px solid #aaa;font-size:10px;padding:3px 8px;font-weight:400}
.bullets{list-style:none;font-size:10px;line-height:19.6px;font-weight:400}
.bullets li:before{content:"";display:inline-block;width:6px;height:6px;border-radius:50%;background:#111;margin-right:9px;vertical-align:1px}
.person-name{font-size:11.5px;font-weight:600}
.person-line{font-size:10px;line-height:16px;font-weight:400}
</style>
</head>
<body>
<div class="stage">

<!-- PAGE 1: Startseite -->
<section class="page" style="left:131px;top:172px;height:2065px">
  <div class="a topbar"><span style="left:283px">☏ +(49) 123.45 67 8-0</span><span style="left:412px">✉ info@systemhaus-brandhoff.de</span></div>
  <div class="a header">
    <div class="a brand">BRANDHOFF<small>IT-SYSTEMHAUS</small></div>
    <div class="a brand-dot"></div>
    <svg class="a" style="left:224px;top:20px" width="11" height="11" viewBox="0 0 12 12"><path d="M1 6 6 1l5 5M2.5 5v6h7V5" fill="none" stroke="#333"/></svg>
    <span class="a nav" style="left:250px">Unternehmen ⌄</span>
    <span class="a nav" style="left:343px">Leistungen ⌄</span>
    <span class="a nav" style="left:421px">Support</span>
    <span class="a nav" style="left:486px">Blog</span>
    <span class="a nav" style="left:533px">Karriere ⌄</span>
  </div>
  <div class="a hero" role="img" aria-label="Erde bei Nacht mit Netzwerklinien">
    <div class="a hero-shade"></div>
    <h1 class="a">IT BETREUUNG</h1>
    <p class="a">Analysieren, Planen, Realisieren: Nach diesem Grundprinzip unterstützen wir Sie - von der Beratung bis hin zur fertigen Lösung, ob Netzwerk und Kommunikationsplattform, ob Hard- oder Software.</p>
    <div class="a btn-blue" style="left:348px;top:192px;width:52px;height:20px;line-height:20px">Mehr</div>
    <div class="a arrow" style="left:18px;top:103px"></div>
    <div class="a arrow" style="left:586px;top:103px"></div>
  </div>
  <div class="a center h-mid" style="left:0;top:378px;width:625px">Die perfekte IT für Ihre Firma -<br>Wie können wir Sie dabei unterstützen?</div>
  <div class="a card" style="left:47px;top:424px">Ich möchte mich vergrößern und suche einen zuverlässigen <b>IT-Dienstleister</b><div class="a btn-out">Mehr</div></div>
  <div class="a card" style="left:226px;top:424px">Ich bin unzufrieden mit meinem jetzigen <b>IT-Dienstleister</b><div class="a btn-out">Mehr</div></div>
  <div class="a card" style="left:406px;top:424px">Ich suche Unterstützung für meine internen <b>IT-Betreuer</b><div class="a btn-out">Mehr</div></div>
  <div class="a hr" style="left:49px;top:591px;width:530px"></div>
  <div class="a media" style="left:49px;top:620px;width:261px;height:147px;background:linear-gradient(135deg,#c9ccd2,#7c8088)" role="img" aria-label="Video: Geschäftsführer stellt das Systemhaus vor"></div>
  <div class="a news-t" style="left:330px;top:622px">Lukas Brandhoff Systemhaus Brandhoff</div>
  <p class="a body-s" style="left:330px;top:649px;width:248px">Systemhaus Brandhoff ist Ihr IT-Dienstleister für Datenschutz, IT-Sicherheit, Netzwerktechnik und mehr. eit 1994 bietet das Systemhaus Brandhoff Ihnen kompetente Betreuung Ihrer gesamten IT-Infrastruktur. Dazu zählt außerdem die Einführung und Schulung Ihrer Mitarbeiter, in den neuen Systemen.Mockup</p>
  <div class="a hr" style="left:49px;top:793px;width:530px"></div>
  <div class="a" style="left:45px;top:811px;font-size:11px;font-weight:400"><span style="color:var(--link)">News</span> &nbsp;|&nbsp; <span style="color:#555">Blogs</span></div>
  <div class="a media" style="left:47px;top:852px;width:217px;height:106px" role="img" aria-label="Team-Foto am Messestand"></div>
  <div class="a news-t" style="left:47px;top:967px">Bergisches Bewerberdating -<br>wir suchen DICH!</div>
  <p class="a" style="left:47px;top:1010px;width:215px;font-size:7.5px;line-height:12.5px">Ausbildung zum/zur:<br>Fachinformatiker/in (m/w/d) für Systemintegration<br>Kaufmann/frau (m/w/d) für Büromanagement<br>IT-Systemkaufmann (m/w/d)....</p>
  <div class="a" style="left:47px;top:1068px;width:53px;height:20px;border:1px solid #777;font-size:7.5px;text-align:center;line-height:18px">Read More</div>
  <div class="a date" style="left:46px;top:1110px">Gelesen 7852 mal</div>
  <div class="a date" style="left:198px;top:1110px">20 Februar 2020</div>
  <div class="a" style="left:273px;top:840px;width:1px;height:282px;background:var(--line)"></div>
  <div class="a media" style="left:316px;top:840px;width:80px;height:56px" role="img" aria-label="Klinikflur"></div>
  <div class="a news-t" style="left:402px;top:845px">Datenleck in Kliniken – altes<br>Dienstkonto war der Grund!</div>
  <div class="a date" style="left:402px;top:886px">22 September 2019</div>
  <div class="a hr" style="left:316px;top:904px;width:264px"></div>
  <div class="a media" style="left:316px;top:913px;width:80px;height:56px;background:linear-gradient(135deg,#f2f2f2,#d6d6d6)" role="img" aria-label="Zertifikat"></div>
  <div class="a news-t" style="left:402px;top:913px">SafeVault Zertifizierung</div>
  <div class="a date" style="left:402px;top:960px">03 Dezember 2019</div>
  <div class="a hr" style="left:316px;top:978px;width:264px"></div>
  <div class="a media" style="left:316px;top:988px;width:80px;height:56px;background:linear-gradient(135deg,#eeeeee,#b9bcc2)" role="img" aria-label="Mitarbeiter im Vertrieb"></div>
  <div class="a news-t" style="left:402px;top:987px">Unterstützung im Vertrieb</div>
  <div class="a date" style="left:402px;top:1034px">09 August 2019</div>
  <div class="a hr" style="left:316px;top:1057px;width:264px"></div>
  <div class="a media" style="left:316px;top:1067px;width:80px;height:60px;background:linear-gradient(135deg,#3c4652,#1e242c)" role="img" aria-label="Smartphone in der Hand"></div>
  <div class="a news-t" style="left:402px;top:1066px">Unbedingt ChatLine<br>updaten – Sicherheitslücke!</div>
  <div class="a date" style="left:402px;top:1117px">14 Mai 2019</div>
  <div class="a center" style="left:0;top:1146px;width:625px;font-size:11px;font-weight:400;color:var(--link)">Alle News</div>
  <div class="a hr" style="left:49px;top:1188px;width:530px"></div>
  <div class="a" style="left:45px;top:1206px;font-size:10.5px;font-weight:400">KUNDENMEINUNGEN</div>
  <div class="a" style="left:361px;top:1206px;font-size:10.5px;font-weight:400">UNVERBINDLICHE ERSTBERATUNG</div>
  <svg class="a" style="left:47px;top:1236px" width="264" height="176" viewBox="0 0 264 176"><path d="M0 0H263V176L240 140H0Z" fill="#f1e2e0"/></svg>
  <div class="a" style="left:70px;top:1248px;width:80px;height:80px;border-radius:50%;background:linear-gradient(160deg,#f5f5f5,#9aa3ad)" role="img" aria-label="Portrait Kunde"></div>
  <div class="a" style="left:143px;top:1256px;font-size:11px;font-weight:400">Jonas Kellner</div>
  <div class="a" style="left:143px;top:1272px;font-size:7.5px;font-style:italic">Head of Realization/ Production/ IT</div>
  <p class="a" style="left:143px;top:1293px;width:158px;font-size:7.5px;line-height:12.5px">"Wir schätzen Systemhaus Brandhoff als unseren IT-Spezialisten wegen der praxisorientierten Problemlösungen, der guten Erreichbarkeit und des hohen Engagements."</p>
  <svg class="a" style="left:152px;top:1384px" width="54" height="10"><g fill="#c7bfc4"><circle cx="5" cy="5" r="4" fill="#9e979b"/><circle cx="16" cy="5" r="4"/><circle cx="27" cy="5" r="4"/><circle cx="38" cy="5" r="4"/><circle cx="49" cy="5" r="4"/></g></svg>
  <div class="a input" style="left:360px;top:1241px">Ihr Name*</div>
  <div class="a input" style="left:360px;top:1263px">Ihre Firma</div>
  <div class="a input" style="left:360px;top:1284px">Ihre E-Mail Adresse*</div>
  <div class="a input" style="left:360px;top:1306px">Ihre Telefonnummer</div>
  <div class="a input" style="left:360px;top:1327px;height:37px">Ihre Anfrage</div>
  <div class="a btn-blue" style="left:360px;top:1374px;width:219px;height:15px;line-height:15px;font-size:8px">IT-Betreuung anfragen</div>
  <div class="a" style="left:361px;top:1396px;width:8px;height:8px;border:1px solid #999"></div>
  <p class="a" style="left:374px;top:1395px;width:205px;font-size:5.5px;line-height:9.5px">*Sie erklären sich damit einverstanden, dass Ihre Daten zur Bearbeitung Ihres Anliegens verwendet werden. Informationen und Widerrufshinweise finden Sie in der <span style="color:var(--link)">Datenschutzerklärung</span>.</p>
  <div class="a" style="left:360px;top:1432px;width:86px;height:50px;border:1px solid #ccc;background:#fafafa" role="img" aria-label="Sicherheitsgrafik"></div>
  <div class="a input" style="left:360px;top:1487px;width:86px;font-size:6px">Sicherheitscode*</div>
  <div class="a" style="left:0;top:1534px;width:625px;height:151px;background:var(--band)"></div>
  <div class="a center" style="left:0;top:1557px;width:625px;font-size:10px;font-weight:400">IT BETREUUNG FÜR...</div>
  <div class="a center" style="left:0;top:1610px;width:625px;word-spacing:0"><span class="city">Solingen</span>&emsp;&emsp;<span class="city">Haan</span>&emsp;&emsp;<span class="city">Hilden</span>&emsp;&emsp;<span class="city">Langenfeld</span>&emsp;&emsp;<span class="city">Monheim</span>&emsp;&emsp;<span class="city">Remscheid</span></div>
  <div class="a center" style="left:0;top:1648px;width:625px"><span class="city">Wuppertal</span>&emsp;&emsp;<span class="city">Leverkusen</span>&emsp;&emsp;<span class="city">Leichlingen</span>&emsp;&emsp;<span class="city">Köln</span>&emsp;&emsp;<span class="city">Velbert</span>&emsp;&emsp;<span class="city">Wermelskirchen</span></div>
  <div class="a center" style="left:0;top:1711px;width:625px;font-size:11px;font-weight:400">Wir sind an verschiedenen Standorten für Sie da.</div>
  <div class="a center" style="left:0;top:1743px;width:625px;font-size:7.5px">Ob vor Ort oder per Fernwartung - unsere Mitarbeiter stellen sich ganz auf Sie und Ihr Unternehmen ein.</div>
  <div class="a footer" style="top:1855px">
    <div class="a brand">BRANDHOFF<small>IT-SYSTEMHAUS</small></div>
    <div class="a f-big" style="left:46px;top:48px">Systemhaus Brandhoff GmbH<br>&amp; Co. KG</div>
    <div class="a f-s" style="left:46px;top:82px">Lindenweg 12<br>12345 Musterstadt<br><br>Fax: +(49) 123.45 67 8-20<br>E-Mail: info@systemhaus-brandhoff.de<br>Web: www.systemhaus-brandhoff.de</div>
    <div class="a f-big" style="left:228px;top:48px">Telefon:<br>+(49) 123.45 67 8-0</div>
    <div class="a f-s" style="left:228px;top:92px">Unsere Geschäftszeiten sind<br>(ausser in Supportfällen):<br><br>Montag - Donnerstag: 08:00 - 17:00 Uhr<br>Freitag: 08:00 - 16:00 Uhr</div>
    <div class="a" style="left:397px;top:50px;font-size:10px;font-weight:400">QUICK LINKS</div>
    <div class="a f-link" style="left:397px;top:65px">Unternehmen ⌄<br>Leistungen ⌄<br>Support<br>Blog<br>Karrierre ⌄</div>
    <div class="a f-r" style="left:488px;top:43px">▭ Fernwartung<br>▪ Feedback<br>● IT-Notfall melden</div>
    <div class="a" style="left:488px;top:119px"><span class="sq"></span><span class="sq"></span><span class="sq"></span><span class="sq"></span></div>
    <div class="a center" style="left:0;top:186px;width:625px;font-size:9px;font-weight:400">2022 © Systemhaus Brandhoff GmbH &amp; Co. KG</div>
  </div>
</section>

<!-- PAGE 2: Leistungen / IT Betreuung -->
<section class="page" style="left:777px;top:172px;height:936px">
  <div class="a topbar"><span style="left:283px">☏ +(49) 123.45 67 8-0</span><span style="left:412px">✉ info@systemhaus-brandhoff.de</span></div>
  <div class="a header">
    <div class="a brand">BRANDHOFF<small>IT-SYSTEMHAUS</small></div>
    <div class="a brand-dot"></div>
    <svg class="a" style="left:224px;top:20px" width="11" height="11" viewBox="0 0 12 12"><path d="M1 6 6 1l5 5M2.5 5v6h7V5" fill="none" stroke="#333"/></svg>
    <span class="a nav" style="left:250px">Unternehmen ⌄</span>
    <span class="a nav" style="left:343px">Leistungen ⌄</span>
    <span class="a nav" style="left:421px">Support</span>
    <span class="a nav" style="left:486px">Blog</span>
    <span class="a nav" style="left:533px">Karriere ⌄</span>
  </div>
  <div class="a crumb" style="left:40px;top:150px">⌂ › Leistungen › IT Betreuung</div>
  <div class="a select" style="left:405px;top:156px">Leistungen <span style="float:right">⇕</span></div>
  <div class="a" style="left:45px;top:208px;width:175px;height:112px;background:linear-gradient(135deg,#f2f4f7,#c8d3e2)" role="img" aria-label="Website auf Bildschirm, Tablet und Smartphone"></div>
  <div class="a" style="left:245px;top:206px;font-size:16px;font-weight:400">IT BETREUUNG</div>
  <p class="a body-s" style="left:250px;top:239px;width:335px">Kundenbetreuung mit Erfahrung<br>Seit 1994 bietet das Systemhaus Brandhoff Ihnen kompetente Betreuung Ihrer gesamten IT-Infrastruktur. Dazu zählt außerdem die Einführung und Schulung Ihrer Mitarbeiter, in den neuen Systemen.Mockup<br><br>Mit uns als Ihr EDV-Partner können Sie sich auf Ihr Kerngeschäft konzentrieren.</p>
  <div class="a" style="left:45px;top:382px;font-size:11px;font-weight:400">Zu unseren Leistungen der IT-Betreuung zählen unter anderem:</div>
  <ul class="a bullets" style="left:70px;top:414px">
    <li>Bundesweiter Service</li><li>Persönliche Betreuung</li><li>Fernwartung</li><li>IT-Notfallservice</li><li>IT Dokumentation</li><li>Ticket System</li><li>Serverüberwachung</li><li>Reparatur Service</li><li>Leasing</li><li>Service Card</li><li>Service- und Wartungsverträge</li>
  </ul>
  <div class="a footer" style="top:725px">
    <div class="a brand">BRANDHOFF<small>IT-SYSTEMHAUS</small></div>
    <div class="a f-big" style="left:46px;top:48px">Systemhaus Brandhoff GmbH<br>&amp; Co. KG</div>
    <div class="a f-s" style="left:46px;top:82px">Lindenweg 12<br>12345 Musterstadt<br><br>Fax: +(49) 123.45 67 8-20<br>E-Mail: info@systemhaus-brandhoff.de<br>Web: www.systemhaus-brandhoff.de</div>
    <div class="a f-big" style="left:228px;top:48px">Telefon:<br>+(49) 123.45 67 8-0</div>
    <div class="a f-s" style="left:228px;top:92px">Unsere Geschäftszeiten sind<br>(ausser in Supportfällen):<br><br>Montag - Donnerstag: 08:00 - 17:00 Uhr<br>Freitag: 08:00 - 16:00 Uhr</div>
    <div class="a" style="left:397px;top:50px;font-size:10px;font-weight:400">QUICK LINKS</div>
    <div class="a f-link" style="left:397px;top:65px">Unternehmen ⌄<br>Lestungen ⌄<br>Support<br>Blog<br>Karrierre ⌄</div>
    <div class="a f-r" style="left:488px;top:43px">▭ Fernwartung<br>▪ Feedback<br>● IT-Notfall melden</div>
    <div class="a" style="left:488px;top:119px"><span class="sq"></span><span class="sq"></span><span class="sq"></span><span class="sq"></span></div>
    <div class="a center" style="left:0;top:186px;width:625px;font-size:9px;font-weight:400">2022 © Systemhaus Brandhoff GmbH &amp; Co. KG</div>
  </div>
</section>

<!-- PAGE 3: Unternehmen / Management -->
<section class="page" style="left:777px;top:1137px;height:936px">
  <div class="a topbar"><span style="left:283px">☏ +(49) 123.45 67 8-0</span><span style="left:412px">✉ info@systemhaus-brandhoff.de</span></div>
  <div class="a header">
    <div class="a brand">BRANDHOFF<small>IT-SYSTEMHAUS</small></div>
    <div class="a brand-dot"></div>
    <svg class="a" style="left:224px;top:20px" width="11" height="11" viewBox="0 0 12 12"><path d="M1 6 6 1l5 5M2.5 5v6h7V5" fill="none" stroke="#333"/></svg>
    <span class="a nav" style="left:250px">Unternehmen ⌄</span>
    <span class="a nav" style="left:343px">Leistungen ⌄</span>
    <span class="a nav" style="left:421px">Support</span>
    <span class="a nav" style="left:486px">Blog</span>
    <span class="a nav" style="left:533px">Karriere ⌄</span>
  </div>
  <div class="a crumb" style="left:44px;top:150px">⌂ › Unternehmen › Management</div>
  <div class="a select" style="left:405px;top:156px">Unternehmen <span style="float:right">⇕</span></div>
  <div class="a center" style="left:0;top:195px;width:625px;font-size:15px;font-weight:600">Geschäftsführung</div>
  <div class="a" style="left:200px;top:246px;width:55px;height:66px;background:linear-gradient(160deg,#cfd3d8,#7d858f)" role="img" aria-label="Portrait Geschäftsführer"></div>
  <div class="a person-name" style="left:262px;top:246px">Lukas Brandhoff</div>
  <div class="a person-line" style="left:262px;top:261px">Geschäftsführer<br>☏ 0123 45678 - 0<br>✉ lb@systemhaus-brandhoff.de</div>
  <div class="a" style="left:198px;top:349px;width:55px;height:68px;background:linear-gradient(160deg,#b7bdc4,#6f5f58)" role="img" aria-label="Portrait stellvertretender Geschäftsführer"></div>
  <div class="a person-name" style="left:260px;top:348px">Peter Lindner</div>
  <div class="a person-line" style="left:260px;top:363px">stellvertretender Geschäftsführer<br>☏ 0123 45678 - 12<br>✉ pl@systemhaus-brandhoff.de</div>
  <div class="a footer" style="top:725px">
    <div class="a brand">BRANDHOFF<small>IT-SYSTEMHAUS</small></div>
    <div class="a f-big" style="left:46px;top:48px">Systemhaus Brandhoff GmbH<br>&amp; Co. KG</div>
    <div class="a f-s" style="left:46px;top:82px">Lindenweg 12<br>12345 Musterstadt<br><br>Fax: +(49) 123.45 67 8-20<br>E-Mail: info@systemhaus-brandhoff.de<br>Web: www.systemhaus-brandhoff.de</div>
    <div class="a f-big" style="left:228px;top:48px">Telefon:<br>+(49) 123.45 67 8-0</div>
    <div class="a f-s" style="left:228px;top:92px">Unsere Geschäftszeiten sind<br>(ausser in Supportfällen):<br><br>Montag - Donnerstag: 08:00 - 17:00 Uhr<br>Freitag: 08:00 - 16:00 Uhr</div>
    <div class="a" style="left:397px;top:50px;font-size:10px;font-weight:400">QUICK LINKS</div>
    <div class="a f-link" style="left:397px;top:65px">Unternehmen ⌄<br>Lestungen ⌄<br>Support<br>Blog<br>Karrierre ⌄</div>
    <div class="a f-r" style="left:488px;top:43px">▭ Fernwartung<br>▪ Feedback<br>● IT-Notfall melden</div>
    <div class="a" style="left:488px;top:119px"><span class="sq"></span><span class="sq"></span><span class="sq"></span><span class="sq"></span></div>
    <div class="a center" style="left:0;top:186px;width:625px;font-size:9px;font-weight:400">2022 © Systemhaus Brandhoff GmbH &amp; Co. KG</div>
  </div>
</section>

</div>
</body>
</html>
```